Business Card Design

I am a voice actor and need a business card to match the design of my website, www.taralundgren.example. The colors are red, black and white. I've attached a pic of the back of a business card I thought was cool that for my design, could maybe have the black and white background from my website and the website address going across the middle of the card in red...or within a red square and white lettering..?? Just play around with it. Also wanting to keep the fonts on the business card similar to those on the website. I also attached a copy of the front of a business card that I liked. My design does not have to look like this.
I have a tag line, but not sure it will be too much to add to my business card or not. Would like to see the design with the tag and without it. "Spoken from Within..." you'll see it on my website.
I will be ordering additional items from the chosen designer. I need a nice logo to use on my invoices, notecards and I need a letterhead design. Thank you so much for being artistically brilliant!
Industry/Entity Type
Business
Contact Information for Business Card
Tara Lundgren
Voice Actor
Email: Tara@TaraLundgren.example
Website: www.TaraLundgren.example
Look and feel

```html
<!DOCTYPE html>
<html lang="en">
<head>
<meta charset="utf-8">
<title>Tara Lundgren – Voice Actor Business Card</title>
<link rel="stylesheet" href="https://fonts.googleapis.com/css2?family=Abril+Fatface&family=Marcellus&family=Cormorant+Garamond:ital,wght@1,500&display=swap">
<style>
  :root {
    --card-red: #980000;
    --ink-white: #ffffff;
    --page-black: #111111;
  }
  html, body {
    margin: 0;
    padding: 0;
    width: 1200px;
    height: 704px;
    overflow: hidden;
    background: var(--page-black);
  }
  .card {
    position: absolute;
    left: 14px;
    top: 12px;
    width: 1172px;
    height: 680px;
    background: var(--card-red);
    border-radius: 9px;
    color: var(--ink-white);
  }
  .card-frame {
    position: absolute;
    left: 47px;
    top: 45px;
    width: 1078px;
    height: 588px;
    border: 2px dashed rgba(255,255,255,0.9);
    box-sizing: border-box;
  }
  .ornament-band {
    position: absolute;
    left: 179px;
    width: 807px;
    height: 56px;
    background: linear-gradient(90deg,
      rgba(255,255,255,0) 0%,
      rgba(255,255,255,0.35) 35%,
      rgba(255,255,255,0.6) 50%,
      rgba(255,255,255,0.35) 65%,
      rgba(255,255,255,0) 100%);
  }
  .ornament-top { top: 125px; }
  .ornament-bottom { top: 500px; }
  .card-line {
    position: absolute;
    left: 0;
    width: 1172px;
    margin: 0;
    text-align: center;
    white-space: nowrap;
  }
  .name {
    top: 183px;
    font-family: "Abril Fatface", serif;
    font-weight: 400;
    font-size: 90px;
    line-height: 100px;
  }
  .role {
    top: 290px;
    font-family: "Marcellus", serif;
    font-size: 46px;
    letter-spacing: 4px;
    line-height: 56px;
  }
  .email {
    top: 370px;
    font-family: "Cormorant Garamond", serif;
    font-style: italic;
    font-weight: 500;
    font-size: 50px;
    line-height: 56px;
  }
  .website {
    top: 430px;
    font-family: "Marcellus", serif;
    font-size: 28px;
    letter-spacing: 2px;
    line-height: 36px;
  }
</style>
</head>
<body>
<main class="card">
  <div class="card-frame"></div>

  <div class="ornament-band ornament-top" role="img" aria-label="Decorative divider: a row of three stars between dotted rules"></div>

  <h1 class="card-line name">Tara Lundgren</h1>
  <p class="card-line role">Voice Actor</p>
  <p class="card-line email">Tara@TaraLundgren.example</p>
  <p class="card-line website">www.TaraLundgren.example</p>

  <div class="ornament-band ornament-bottom" role="img" aria-label="Decorative divider: a row of three stars between dotted rules"></div>
</main>
</body>
</html>
```